Marlow Crest Group (Real Estate and Investment)

A high end, clean design.
We are a real estate company with sales, asset management and investment divisions. We want to use a black and white scheme which is really high end feel. The back of the card can just be the logo (black background with the white writing) as we will probably emboss this when we print)

Target Market(s)

High level investors, high end houses for sale

Industry/Entity Type

Business

Contact Information for Business Card

Name, position, phone number and email address
Glen Varley, Managing Director, 0437259064 and glen@marlowcrest-example.com.au

Requirements
Must have
• Back of the card to be the black background with the white writing (as per the attached images). Would like the capacity to emboss the writing and logo

```html
<!DOCTYPE html>
<html lang="en">
<head>
<meta charset="utf-8">
<title>Marlow Crest Group – Business Card</title>
<link rel="stylesheet" href="https://fonts.googleapis.com/css2?family=Inter:wght@300&family=Open+Sans:wght@400;700&display=swap">
<style>
  :root {
    --ink: #000000;
    --paper: #ffffff;
    --page: #ffffff;
    --edge: #1a1a1a;
  }
  * { margin: 0; padding: 0; box-sizing: border-box; }
  html, body {
    width: 1074px;
    height: 1200px;
    overflow: hidden;
    background: var(--page);
  }
  .sheet {
    position: relative;
    width: 1074px;
    height: 1200px;
  }
  .card {
    position: absolute;
    left: 113px;
    width: 848px;
    height: 449px;
  }
  .card--front {
    top: 136px;
    background: var(--paper);
    border: 1px solid var(--edge);
  }
  .card--back {
    top: 615px;
    background: var(--ink);
  }
  .holder {
    position: absolute;
    left: 32px;
    top: 32px;
    font-family: "Open Sans", Arial, sans-serif;
    color: var(--ink);
  }
  .holder__name {
    font-weight: 700;
    font-size: 30px;
    line-height: 36px;
  }
  .holder__role {
    font-weight: 400;
    font-size: 22px;
    line-height: 28px;
  }
  .brand-mark {
    position: absolute;
    left: 50%;
    transform: translateX(-50%);
  }
  .card--front .brand-mark { top: 74px; }
  .card--back .brand-mark { top: 98px; }
  .brand-name {
    position: absolute;
    left: 0;
    width: 100%;
    text-align: center;
    font-family: "Inter", Arial, sans-serif;
    font-weight: 300;
    font-size: 38px;
    letter-spacing: 0.5px;
    white-space: nowrap;
  }
  .card--front .brand-name { top: 274px; color: var(--ink); }
  .card--back .brand-name { top: 300px; color: var(--paper); }
  .contact-band {
    position: absolute;
    left: 0;
    bottom: 0;
    width: 100%;
    height: 67px;
    background: var(--ink);
    color: var(--paper);
    font-family: "Open Sans", Arial, sans-serif;
    font-size: 20px;
  }
  .contact-band__phone {
    position: absolute;
    left: 98px;
    top: 0;
    height: 67px;
    display: flex;
    align-items: center;
    gap: 8px;
  }
  .contact-band__email {
    position: absolute;
    right: 55px;
    top: 0;
    line-height: 67px;
  }
</style>
</head>
<body>
<main class="sheet">

  <section class="card card--front" aria-label="Business card front">
    <div class="holder">
      <p class="holder__name">Glen Varley</p>
      <p class="holder__role">Managing Director</p>
    </div>

    <svg class="brand-mark" width="170" height="170" viewBox="0 0 170 170" aria-hidden="true">
      <circle cx="85" cy="85" r="82" fill="none" stroke="var(--ink)" stroke-width="2.5"/>
    </svg>
    <p class="brand-name">MARLOW CREST GROUP</p>

    <div class="contact-band">
      <div class="contact-band__phone">
        <svg width="26" height="30" viewBox="0 0 24 28" aria-hidden="true">
          <path d="M5 2 L9 1 L11 8 L8 10 Q10 16 14 20 L17 18 L22 23 L19 26 Q12 27 6 17 Q2 9 5 2 Z"
                fill="none" stroke="var(--paper)" stroke-width="1.6" stroke-linejoin="round"/>
        </svg>
        <span>0437259064</span>
      </div>
      <span class="contact-band__email">glen@marlowcrest-example.com.au</span>
    </div>
  </section>

  <section class="card card--back" aria-label="Business card back">
    <svg class="brand-mark" width="170" height="170" viewBox="0 0 170 170" aria-hidden="true">
      <circle cx="85" cy="85" r="82" fill="none" stroke="var(--paper)" stroke-width="2.5"/>
    </svg>
    <p class="brand-name">MARLOW CREST GROUP</p>
  </section>

</main>
</body>
</html>
```